Korvell Plant Services

We are a heavy diesel mechanical business with additional air con certificates, remapping engine rebuilt

Contact Information for Business Card

Company Name, Director Name, Managing Director, Contact details, email and website

Font styles to use
Serif
Script

```html
<!DOCTYPE html>
<html lang="en">
<head>
<meta charset="utf-8">
<title>Korvell Plant Services – Business Card</title>
<link rel="stylesheet" href="https://fonts.googleapis.com/css2?family=Cormorant+Garamond:wght@600&family=Montserrat:wght@400;500;800&display=swap">
<style>
  :root {
    --stage: #b3b3b3;
    --card: #ffffff;
    --navy: #06066b;
    --ink: #000000;
    --paper-text: #ffffff;
    --name-grey: #4a4a4a;
  }
  * { box-sizing: border-box; margin: 0; padding: 0; }
  html, body { width: 1200px; height: 900px; overflow: hidden; }
  body { background: var(--stage); position: relative; font-family: "Montserrat", sans-serif; }

  .card {
    position: absolute;
    left: 309px;
    width: 583px;
    height: 341px;
    background: var(--card);
    overflow: hidden;
  }
  .card--front { top: 55px; }
  .card--back { top: 486px; }

  .brand {
    position: absolute;
    display: flex;
    align-items: center;
    color: var(--navy);
    font-weight: 800;
  }
  .brand__dot {
    border-radius: 50%;
    background: var(--ink);
    flex: none;
  }
  .brand__name { line-height: 1.05; }
  .brand__name span { display: block; }

  .card--front .brand { left: 130px; top: 112px; gap: 18px; }
  .card--front .brand__dot { width: 34px; height: 34px; }
  .card--front .brand__name { font-size: 44px; }
  .card--front .brand__name .brand__sub { font-size: 28px; }

  .card--back .brand { left: 192px; top: 64px; gap: 10px; }
  .card--back .brand__dot { width: 18px; height: 18px; }
  .card--back .brand__name { font-size: 25px; }
  .card--back .brand__name .brand__sub { font-size: 16px; }

  .wave { position: absolute; inset: 0; width: 583px; height: 341px; }

  .contacts {
    position: absolute;
    left: 56px;
    top: 209px;
    list-style: none;
    color: var(--paper-text);
    font-size: 13px;
    font-weight: 500;
    letter-spacing: 0.3px;
  }
  .contacts li {
    display: flex;
    align-items: center;
    gap: 13px;
    height: 23px;
    margin-bottom: 10.5px;
  }
  .contacts svg { width: 23px; height: 23px; flex: none; }

  .director {
    position: absolute;
    left: 332px;
    top: 233px;
  }
  .director__name {
    font-family: "Cormorant Garamond", serif;
    font-weight: 600;
    font-size: 23px;
    color: var(--name-grey);
    line-height: 1;
  }
  .director__role {
    font-size: 11px;
    color: var(--paper-text);
    letter-spacing: 0.2px;
  }
</style>
</head>
<body>

<section class="card card--front">
  <div class="brand">
    <div class="brand__dot"></div>
    <div class="brand__name">
      <span>Korvell</span>
      <span class="brand__sub">Plant Services</span>
    </div>
  </div>
</section>

<section class="card card--back">
  <svg class="wave" viewBox="0 0 583 341" aria-hidden="true">
    <path d="M0 143 Q 300 205 583 144 L583 341 L0 341 Z" fill="var(--navy)"/>
    <path d="M0 173 Q 250 215 583 144 L583 341 L0 341 Z" fill="var(--ink)"/>
  </svg>

  <div class="brand">
    <div class="brand__dot"></div>
    <div class="brand__name">
      <span>Korvell</span>
      <span class="brand__sub">Plant Services</span>
    </div>
  </div>

  <ul class="contacts">
    <li>
      <svg viewBox="0 0 24 24" aria-hidden="true"><circle cx="12" cy="12" r="10.8" fill="none" stroke="#fff" stroke-width="1.6"/><path d="M8.6 7.2c.6-.4 1.1-.3 1.4.2l1 1.7c.3.5.2.9-.2 1.2l-.7.5c.4 1.2 1.4 2.3 2.6 2.8l.5-.7c.3-.4.8-.5 1.2-.2l1.7 1c.5.3.6.9.2 1.4-.8 1-1.8 1.3-3 .8-2.4-1-4.3-3-5.2-5.4-.4-1.2 0-2.4.5-3.3z" fill="#fff"/></svg>
      <span>012 345 7890</span>
    </li>
    <li>
      <svg viewBox="0 0 24 24" aria-hidden="true"><circle cx="12" cy="12" r="10.8" fill="none" stroke="#fff" stroke-width="1.6"/><rect x="7" y="8.5" width="10" height="7" fill="#fff"/><path d="M7 8.5l5 4 5-4M7 15.5l3.6-3.4M17 15.5l-3.6-3.4" fill="none" stroke="#000" stroke-width="0.9"/></svg>
      <span>info@website.com</span>
    </li>
    <li>
      <svg viewBox="0 0 24 24" aria-hidden="true"><circle cx="12" cy="12" r="10.8" fill="none" stroke="#fff" stroke-width="1.6"/><path d="M9.5 6.5v10l2.3-2.2 1.6 3.5 1.4-.6-1.6-3.4h3.2z" fill="#fff"/></svg>
      <span>www.website.com</span>
    </li>
  </ul>

  <div class="director">
    <p class="director__name">DIRECTOR NAME</p>
    <p class="director__role">MANAGING DIRECTOR</p>
  </div>
</section>

</body>
</html>
```